Corrow Family Farm fresh honey jar label

I need a label for jars of honey harvested at our farm. These are for gifts and personal use. We are looking to incorporate our farm brand into the label. We would like the design to take the existing brand and add some element like bees, honey, flowers, or hives to indicate the contents. We want the design to feel homemade and authentic without feeling cheap or hoaky

Requirements
Must have
• The label must be made to fit a 1" x2" rectangular label. The label must include the attached family brand. The label must include the text "Corrow Family Farms" "Pinebrook, USA" "Farm Fresh Honey". The label will be printed on off-white paper
Nice to have
• It would be nice to have illustrations of bees or flowers around the logo or hives or honeycombs. The label should have a vintage feel
Should not have
• The label should not feel overly cartoonish or hoaky

```html
<!DOCTYPE html>
<html lang="en">
<head>
<meta charset="utf-8">
<title>Corrow Family Farms – Farm Fresh Honey Label</title>
<link rel="stylesheet" href="https://fonts.googleapis.com/css2?family=Roboto+Condensed:wght@400;600&family=Work+Sans:wght@500&display=swap">
<style>
  :root {
    --backdrop: #f5e2a6;
    --paper: #f2eee2;
    --ink: #1b1a18;
    --poppy-red: #e2675d;
    --poppy-pink: #efb3b6;
    --leaf: #8fae96;
    --cream-petal: #f4efe6;
  }
  html, body {
    margin: 0;
    width: 1200px;
    height: 1200px;
    overflow: hidden;
    background: var(--backdrop);
  }
  .canvas {
    position: relative;
    width: 1200px;
    height: 1200px;
  }
  .label {
    position: absolute;
    left: 350px;
    top: 100px;
    width: 500px;
    height: 1000px;
    background: var(--paper);
    border-radius: 10px;
    overflow: hidden;
    color: var(--ink);
    text-align: center;
  }
  .brand-mark {
    position: absolute;
    top: 108px;
    left: 0;
    right: 0;
    font-family: "Work Sans", sans-serif;
    font-weight: 500;
    font-size: 50px;
    letter-spacing: 0.12em;
    line-height: 1;
  }
  .farm-name {
    position: absolute;
    top: 258px;
    left: 0;
    right: 0;
    font-family: "Work Sans", sans-serif;
    font-weight: 500;
    font-size: 25px;
    letter-spacing: 0.09em;
    line-height: 1;
  }
  .farm-location {
    position: absolute;
    top: 305px;
    left: 0;
    right: 0;
    font-family: "Roboto Condensed", sans-serif;
    font-weight: 600;
    font-size: 19px;
    letter-spacing: 0.04em;
    line-height: 1;
  }
  .product-title {
    position: absolute;
    top: 415px;
    left: 0;
    right: 0;
    margin: 0;
    font-family: "Roboto Condensed", sans-serif;
    font-weight: 400;
    font-size: 72px;
    line-height: 0.95;
    letter-spacing: 0.01em;
  }
  .floral-art {
    position: absolute;
    left: 0;
    bottom: 0;
    width: 500px;
    height: 440px;
  }
</style>
</head>
<body>
<div class="canvas">
  <div class="label">
    <div class="brand-mark">CORROW</div>
    <div class="farm-name">CORROW FAMILY FARMS</div>
    <div class="farm-location">PINEBROOK, USA</div>
    <h1 class="product-title">FARM FRESH<br>HONEY</h1>
    <svg class="floral-art" viewBox="0 0 500 440" role="img" aria-label="Watercolour illustration of red, pink and white poppies with bees flying around them">
      <defs>
        <radialGradient id="bloom-red" cx="0.3" cy="0.55" r="0.5">
          <stop offset="0" stop-color="var(--poppy-red)" stop-opacity="0.85"/>
          <stop offset="1" stop-color="var(--poppy-red)" stop-opacity="0"/>
        </radialGradient>
        <radialGradient id="bloom-pink" cx="0.6" cy="0.35" r="0.4">
          <stop offset="0" stop-color="var(--poppy-pink)" stop-opacity="0.8"/>
          <stop offset="1" stop-color="var(--poppy-pink)" stop-opacity="0"/>
        </radialGradient>
        <radialGradient id="bloom-leaf" cx="0.2" cy="0.95" r="0.35">
          <stop offset="0" stop-color="var(--leaf)" stop-opacity="0.8"/>
          <stop offset="1" stop-color="var(--leaf)" stop-opacity="0"/>
        </radialGradient>
      </defs>
      <rect width="500" height="440" fill="url(#bloom-leaf)"/>
      <rect width="500" height="440" fill="url(#bloom-pink)"/>
      <rect width="500" height="440" fill="url(#bloom-red)"/>
    </svg>
  </div>
</div>
</body>
</html>
```